依頼詳細
ホームページ料金の価格破壊を行いたいです。納品が1週間以内で早い!!イラストよりも写真を使ってほしいです。
記載項目
社名等も入れますが、上記の内容を考慮して作っていただけると助かります。
よろしくお願いいたします。
サイズ
A4
ページ数
片面
希望イメージ
シンプル 複雑
単色 カラフル
暗い 明るい
日常 高級
遊び心 厳粛
未来的 伝統的
女性的 男性的
希望する色
お任せいたします。
納品ファイル
• 高解像度JPG (.jpg)
• イラストレーター形式 (.ai)
〒471-0093
大阪市淀川区東川原3-4-17
ミツバ第2北梅田4階
0120-914-562
この住所を明記ください。
月々の料金なし!!ポッキリ 5万円!!
プロの作ったホームページが5万円!!みたいな
友達に作ってもらった安かろう悪かろうではなく、本当の高品質なホームページが作れる集団です。みたいなことを入れてほしい。

写真が奇麗でいいなあ!と思いました。

他にも良いデザインがたくさんありました。迷いましたが・・・・みなさんありがとうございました。

```html
<!DOCTYPE html>
<html lang="ja">
<head>
<meta charset="utf-8">
<title>プロが作るホームページ 5万円 | ソラリンク</title>
<link href="https://fonts.googleapis.com/css2?family=Noto+Sans+JP:wght@400;500;700;900&family=Roboto:wght@700;900&display=swap" rel="stylesheet">
<style>
:root{
  --navy:#1c2a6b;
  --navy-deep:#0e1640;
  --blue:#2e4aa8;
  --red:#d0202f;
  --ink:#222;
  --paper:#ffffff;
}
*{margin:0;padding:0;box-sizing:border-box}
html,body{width:846px;height:1200px;overflow:hidden;background:var(--paper)}
body{position:relative;font-family:"Noto Sans JP",sans-serif;color:var(--ink)}
.hero-photo{position:absolute;left:0;top:0;width:846px;height:440px;
  background:radial-gradient(ellipse at 62% 55%,#9aa9cf 0%,#4a5f9e 30%,#1b2a66 62%,var(--navy-deep) 100%)}
.headline{position:absolute;left:40px;top:14px;font-size:68px;font-weight:900;color:#fff;letter-spacing:2px;
  text-shadow:0 3px 8px rgba(0,0,0,.5)}
.price{position:absolute;left:560px;top:120px;width:280px;height:300px;color:#fff;text-shadow:0 3px 10px rgba(0,0,0,.5)}
.price-num{position:absolute;left:0;top:0;font-family:"Roboto",sans-serif;font-weight:900;font-size:250px;line-height:1;font-style:italic}
.price-tax{position:absolute;left:152px;top:86px;font-size:15px;font-weight:700;white-space:nowrap}
.price-unit{position:absolute;left:160px;top:108px;font-size:56px;font-weight:900;line-height:1.1;white-space:nowrap}
.badges{position:absolute;left:22px;top:452px;width:802px;display:flex;gap:10px}
.badge{flex:1;height:58px;background:var(--navy);color:#fff;display:flex;align-items:center;justify-content:center;
  font-size:22px;font-weight:900;line-height:1.1;text-align:center;border:2px solid #fff;box-shadow:0 0 0 2px var(--navy)}
.badge small{display:block;font-size:12px;font-weight:500}
.badge.is-accent{background:var(--red);box-shadow:0 0 0 2px var(--red)}
.col{position:absolute;top:532px}
.col-left{left:22px;width:396px}
.col-right{left:440px;width:384px}
.intro{font-size:14px;font-weight:700;line-height:1.7;margin-bottom:12px}
.section-bar{background:var(--navy);color:#fff;font-size:15px;font-weight:700;padding:4px 10px;margin-bottom:8px}
.body-text{font-size:11.5px;line-height:1.65;margin-bottom:12px}
.price-list{list-style:none;font-size:11px;font-weight:700;color:var(--navy);margin:-4px 0 12px;display:flex;flex-wrap:wrap;gap:4px 14px}
.price-list li::before{content:"";display:inline-block;width:8px;height:8px;background:var(--navy);margin-right:4px}
.work-photo{width:396px;height:156px;background:linear-gradient(135deg,#dfe4ee 0%,#9fb0cf 45%,#4b5f95 100%)}
.led-photo{width:384px;height:110px;background:linear-gradient(135deg,#0e1640 0%,#2e4aa8 60%,#8fa3d8 100%)}
.rule{position:absolute;left:22px;top:968px;width:802px;height:3px;background:var(--navy)}
.logo{position:absolute;left:22px;top:1000px;display:flex;align-items:center;gap:10px}
.logo-mark{width:46px;height:46px;border-radius:50%;background:var(--navy)}
.logo-name{font-size:34px;font-weight:700;color:var(--navy);line-height:1}
.logo-corp{position:absolute;left:78px;top:40px;font-size:11px;color:var(--navy);white-space:nowrap}
.tel{position:absolute;right:22px;top:978px;display:flex;align-items:center;gap:10px;color:var(--navy)}
.tel-num{font-family:"Roboto",sans-serif;font-weight:900;font-size:60px;line-height:1;letter-spacing:1px}
.web{position:absolute;right:22px;top:1052px;font-family:"Roboto",sans-serif;font-weight:900;font-size:38px;color:var(--navy)}
.address{position:absolute;left:300px;top:1112px;font-size:13px;line-height:1.7;color:var(--ink)}
.bottom-band{position:absolute;left:0;bottom:0;width:846px;height:24px;background:var(--navy)}
</style>
</head>
<body>
<div class="hero-photo" role="img" aria-label="ノートパソコンのキーボードを打つ手元の写真"></div>
<h1 class="headline">プロが作るホームページ</h1>
<div class="price">
  <div class="price-num">5</div>
  <div class="price-tax">(税込52,500円)</div>
  <div class="price-unit">万円</div>
</div>

<div class="badges">
  <div class="badge">月々の料金<br>なし</div>
  <div class="badge is-accent"><span>納品が早い!<small>(約1週間)</small></span></div>
  <div class="badge">ドメイン取得<br>込み</div>
  <div class="badge">サーバー設定<br>全て込み</div>
</div>

<section class="col col-left">
  <p class="intro">株式会社ソラリンクでは、現存ユーザー様より好評な支援を頂いております。それぞれのニーズに特化した独自SEO対策、いかに集客できるかにこだわったホームページ作成。<br>便宜インターネット社会と呼ばれる中で、如何にお客様の目を引き、如何にお客様の期待に入るかという所に、弊社は全力を尽くしております。</p>
  <h2 class="section-bar">ホームページ制作</h2>
  <p class="body-text">友達に作ってもらった安かろう悪かろうのホームページではなく、本当に高品質なホームページを作れるプロ集団です。企画から設計、デザイン、公開まで一貫して担当し、ご依頼から約1週間で納品いたします。月々の管理料金は一切かかりません。</p>
  <div class="work-photo" role="img" aria-label="打ち合わせでノートパソコンの画面を指し示す人物の写真"></div>
</section>

<section class="col col-right">
  <h2 class="section-bar">SEO対策</h2>
  <p class="body-text">検索エンジンで上位に表示されるよう、サイトの構造や文章を最適化します。業種や地域に合わせたキーワード選定で、集客につながるホームページを目指します。</p>
  <h2 class="section-bar">名刺作成</h2>
  <p class="body-text">ホームページと統一したデザインの名刺もご用意できます。会社の印象をそろえて、信頼感のある営業ツールに仕上げます。</p>
  <ul class="price-list">
    <li>片面カラー 100枚</li>
    <li>両面カラー 100枚</li>
    <li>ロゴ入り 100枚</li>
  </ul>
  <h2 class="section-bar">LED看板作成</h2>
  <p class="body-text">店舗の顔となるLED看板も制作いたします。遠くからでも目を引く明るい看板で、来店のきっかけを作ります。</p>
  <div class="led-photo" role="img" aria-label="光るLED看板の写真"></div>
</section>

<div class="rule"></div>

<div class="logo">
  <div class="logo-mark"></div>
  <div class="logo-name">sora link</div>
  <div class="logo-corp">株式会社ソラリンク</div>
</div>

<div class="tel">
  <svg width="62" height="46" viewBox="0 0 62 46" aria-hidden="true">
    <rect x="1" y="1" width="60" height="44" rx="8" fill="none" stroke="#1c2a6b" stroke-width="4"/>
    <path d="M14 30c0-12 34-12 34 0l-6 4-5-5v-4c-4-2-8-2-12 0v4l-5 5z" fill="#1c2a6b"/>
  </svg>
  <div class="tel-num">0120-914-562</div>
</div>
<div class="web">www.soralink-web.jp</div>

<p class="address">〒471-0093 大阪市淀川区東川原3-4-17 ミツバ第2北梅田4階<br>TEL：06-6284-3369　FAX：06-6284-3370　E-mail：info@soralink-web.jp</p>

<div class="bottom-band"></div>
</body>
</html>
```